Property Management Services Proposal - Powerpoint template

We need a proposal template for our multifamily property management services. We have a simple/generic handout that we use (uploaded here) but we need something for an actual proposal/client presentation standpoint. A powerpoint file that includes company/team overview, some placeholders for the specific client we would be proposing too, etc. Website is www.quillonpropertyservices.com

Target Market(s)

Residential/Multifamily Property Owners and Investors

Industry/Entity Type

Real Estate

Font styles to use
Sans Serif

Colors
0355a3
f78f20
9d9d9d
ffffff

Requirements
Must have
• Logo, color scheme (orange, navy, gray) - clean look but not overly simple. Placeholders for specific projects, case studies, timelines, photos, graphs, etc.

```html
<!DOCTYPE html>
<html lang="en">
<head>
<meta charset="utf-8">
<title>Quillon Property Services – Proposal Template Overview</title>
<link href="https://fonts.googleapis.com/css2?family=Lato:wght@400;700;900&display=swap" rel="stylesheet">
<style>
:root{
  --orange:#f78f20;
  --orange-dk:#d9661a;
  --navy:#0355a3;
  --navy-dk:#1d3a80;
  --gray:#9d9d9d;
  --gray-lt:#e6e6e6;
  --ink:#5a5a5a;
  --white:#ffffff;
}
html,body{margin:0;width:1200px;height:4000px;overflow:hidden;background:var(--white);font-family:'Lato',sans-serif}
.deck{display:grid;grid-template-columns:repeat(3,384px);grid-auto-rows:216px;gap:47px 14px;padding:12px 9px}
.slide{position:relative;overflow:hidden;background:var(--white);box-shadow:0 1px 4px rgba(0,0,0,.28)}
.framed{box-shadow:inset 0 0 0 5px var(--orange),0 1px 4px rgba(0,0,0,.28)}
.abs{position:absolute}
.title{position:absolute;left:0;right:0;top:12px;margin:0;text-align:center;color:var(--orange);font-weight:700;font-size:14px}
.title::after{content:"";display:block;width:44px;height:2px;margin:5px auto 0;background:linear-gradient(90deg,var(--orange) 0 58%,transparent 58% 68%,var(--navy) 68%)}
.title.left{text-align:left;left:16px;right:auto}
.title.left::after{margin-left:0}
.title.white{color:var(--white)}
.brand{position:absolute;left:10px;bottom:6px;color:var(--orange);font-weight:900;font-size:9px;letter-spacing:.6px}
.brand.light{color:var(--white)}
.num{position:absolute;right:10px;bottom:6px;font-size:6px;color:var(--gray)}
.copy{font-size:5.5px;line-height:1.5;color:var(--ink);margin:0}
.copy.white{color:var(--white)}
.head{font-size:10px;font-weight:700;line-height:1.2;margin:0 0 4px}
.o{color:var(--orange)}.n{color:var(--navy)}.w{color:var(--white)}
.bg-o{background:var(--orange)}.bg-od{background:var(--orange-dk)}.bg-n{background:var(--navy)}.bg-nd{background:var(--navy-dk)}.bg-g{background:var(--gray)}.bg-gl{background:var(--gray-lt)}
.ph-city{background:linear-gradient(160deg,#5b7fa8,#c9a77a 60%,#3a3f4a)}
.ph-warm{background:linear-gradient(150deg,#d7a363,#6b4a33)}
.ph-sky{background:linear-gradient(180deg,#8fb3d6,#d8dde3 55%,#6d7582)}
.ph-office{background:linear-gradient(135deg,#e3e6ea,#8a8f96)}
.ph-night{background:linear-gradient(170deg,#2d4f7e,#c78a42 70%,#3c2e26)}
.ph-person{background:linear-gradient(180deg,#b9bcc1,#5e6268)}
.ph-device{background:linear-gradient(160deg,#3a3f47,#9aa3ad)}
.ph-map{background:linear-gradient(135deg,#f3d6b4,#eab57c)}
.ph-street{background:linear-gradient(170deg,#e9e1d4,#a58d6d)}
.icon{position:absolute;width:28px;height:28px;background:var(--orange);display:flex;align-items:center;justify-content:center}
.icon svg{width:16px;height:16px;fill:var(--white)}
.icon.navy{background:var(--navy)}
.tile{position:absolute;color:var(--white);padding:6px;box-sizing:border-box}
.tile svg{width:14px;height:14px;fill:var(--white);display:block;margin:0 auto 4px}
.tile .lbl{font-size:6.5px;font-weight:700;text-align:center;margin:0 0 3px}
.tile .copy{text-align:center}
.label{font-size:6.5px;font-weight:700;margin:0}
.bar-row{position:absolute;height:14px;border:1px solid #d0d0d0;box-sizing:border-box}
.badge{position:absolute;width:14px;height:14px;background:var(--orange);color:var(--white);font-size:7px;font-weight:700;display:flex;align-items:center;justify-content:center}
.social{display:flex;gap:4px}
.social span{width:12px;height:12px;background:var(--navy);display:block}
.cell{font-size:5.5px;padding:0 4px;display:flex;align-items:center;box-sizing:border-box;height:13px}
</style>
</head>
<body>
<svg width="0" height="0" style="position:absolute">
  <defs>
    <symbol id="i-house" viewBox="0 0 24 24"><path d="M3 11 12 3l9 8h-3v9h-4v-6h-4v6H6v-9z"/></symbol>
    <symbol id="i-chart" viewBox="0 0 24 24"><path d="M4 20V11h3v9zm6 0V5h3v15zm6 0v-7h3v7z"/></symbol>
    <symbol id="i-truck" viewBox="0 0 24 24"><path d="M2 6h12v10H2zm13 3h4l3 3v4h-7z"/><circle cx="6" cy="18" r="2"/><circle cx="18" cy="18" r="2"/></symbol>
    <symbol id="i-gear" viewBox="0 0 24 24"><path d="M10 2h4v3l2 1 2-2 3 3-2 2 1 2h3v4h-3l-1 2 2 2-3 3-2-2-2 1v3h-4v-3l-2-1-2 2-3-3 2-2-1-2H1v-4h3l1-2-2-2 3-3 2 2 2-1zm2 7a3 3 0 1 0 0 6 3 3 0 0 0 0-6z"/></symbol>
    <symbol id="i-user" viewBox="0 0 24 24"><path d="M12 12a4 4 0 1 0 0-8 4 4 0 0 0 0 8zm-8 9c0-4 4-6 8-6s8 2 8 6z"/></symbol>
    <symbol id="i-pin" viewBox="0 0 24 24"><path d="M12 2a7 7 0 0 0-7 7c0 5 7 13 7 13s7-8 7-13a7 7 0 0 0-7-7zm0 10a3 3 0 1 1 0-6 3 3 0 0 1 0 6z"/></symbol>
    <symbol id="i-check" viewBox="0 0 24 24"><path d="M9 16 4 11l-2 2 7 7L22 7l-2-2z"/></symbol>
    <symbol id="i-phone" viewBox="0 0 24 24"><path d="M6 2h4l2 5-3 2a11 11 0 0 0 6 6l2-3 5 2v4a2 2 0 0 1-2 2C10 20 4 14 4 4a2 2 0 0 1 2-2z"/></symbol>
  </defs>
</svg>

<main class="deck">

<!-- Row 1 -->
<section class="slide framed">
  <div class="abs ph-night" style="inset:0" role="img" aria-label="Photo of a city skyline at dusk"></div>
  <div class="abs bg-o" style="left:120px;top:52px;width:144px;height:96px;padding:12px;box-sizing:border-box;color:#fff">
    <p class="head" style="font-size:14px;font-weight:900">LOREM IPSUM</p>
    <p class="copy white">Lorem ipsum dolor sit amet</p>
    <p style="margin:10px 0 0;font-weight:900;font-size:13px;letter-spacing:1px">QPS</p>
  </div>
</section>

<section class="slide">
  <div class="abs ph-sky" style="left:0;top:0;width:384px;height:216px" role="img" aria-label="Photo of residential towers and autumn trees"></div>
  <div class="abs" style="left:0;top:0;width:150px;height:216px;background:rgba(90,100,115,.85);padding:30px 16px;box-sizing:border-box">
    <p class="head o" style="font-size:15px;font-weight:900">LOREM IPSUM</p>
    <p class="copy white">Lorem ipsum dolor sit amet</p>
    <p class="o" style="margin:60px 0 0;font-weight:900;font-size:16px;letter-spacing:1px">QPS</p>
  </div>
</section>

<section class="slide">
  <h2 class="title left" style="left:150px">Lorem ipsum dolor sit amet</h2>
  <div class="badge" style="left:40px;top:52px">1</div><div class="bar-row" style="left:60px;top:52px;width:280px"></div>
  <div class="badge" style="left:40px;top:76px">2</div><div class="bar-row" style="left:60px;top:76px;width:280px"></div>
  <div class="badge" style="left:40px;top:100px">3</div><div class="bar-row" style="left:60px;top:100px;width:280px"></div>
  <div class="badge" style="left:40px;top:124px">4</div><div class="bar-row" style="left:60px;top:124px;width:280px"></div>
  <div class="badge" style="left:40px;top:148px">5</div><div class="bar-row" style="left:60px;top:148px;width:280px"></div>
  <span class="brand">QPS</span><span class="num">3</span>
</section>

<!-- Row 2 -->
<section class="slide">
  <div class="abs ph-street" style="left:10px;top:10px;width:110px;height:170px" role="img" aria-label="Photo of a city street at evening"></div>
  <h2 class="title left" style="left:135px;top:14px">Lorem ipsum dolor sit amet</h2>
  <div class="abs" style="left:135px;top:48px;width:235px">
    <p class="copy"><b class="o">Lorem ipsum dolor sit amet, consectetur adipiscing elit.</b> Sed do eiusmod tempor incididunt ut labore et dolore magna aliqua.</p>
    <p class="copy" style="margin-top:5px">• Lorem ipsum dolor sit amet, consectetur adipiscing elit.<br>• Sed do eiusmod tempor incididunt ut labore.<br>• Ut enim ad minim veniam, quis nostrud.<br>• Duis aute irure dolor in reprehenderit.</p>
    <p class="copy" style="margin-top:5px">Excepteur sint occaecat cupidatat non proident, sunt in culpa qui officia deserunt mollit anim id est laborum.</p>
  </div>
  <span class="brand">QPS</span><span class="num">4</span>
</section>

<section class="slide">
  <h2 class="title" style="right:130px">Lorem ipsum dolor sit amet</h2>
  <div class="abs" style="left:16px;top:52px;width:220px">
    <p class="copy">Lorem ipsum dolor sit amet, consectetur adipiscing elit, sed do eiusmod tempor incididunt ut labore et dolore magna aliqua. Ut enim ad minim veniam, quis nostrud exercitation.</p>
    <p class="copy" style="margin-top:5px">Duis aute irure dolor in reprehenderit in voluptate velit esse cillum dolore eu fugiat nulla pariatur.</p>
  </div>
  <div class="abs ph-city" style="left:250px;top:14px;width:124px;height:180px" role="img" aria-label="Photo of office towers"></div>
  <span class="brand">QPS</span><span class="num">5</span>
</section>

<section class="slide">
  <div class="abs ph-office" style="left:10px;top:10px;width:110px;height:110px" role="img" aria-label="Photo of a modern building facade"></div>
  <h2 class="title left" style="left:135px">Lorem ipsum dolor sit amet</h2>
  <div class="abs" style="left:135px;top:48px;width:235px">
    <p class="copy">Lorem ipsum dolor sit amet, consectetur adipiscing elit, sed do eiusmod tempor incididunt ut labore et dolore magna aliqua.</p>
  </div>
  <div class="abs ph-sky" style="left:120px;top:140px;width:264px;height:50px" role="img" aria-label="Photo of a glass building reflecting the sky"></div>
  <span class="brand">QPS</span><span class="num">6</span>
</section>

<!-- Row 3 -->
<section class="slide">
  <div class="abs" style="left:12px;top:18px;width:100px">
    <p class="head o">Lorem ipsum</p>
    <p class="copy">Lorem ipsum dolor sit amet, consectetur adipiscing elit, sed do eiusmod tempor.</p>
    <div style="display:flex;gap:5px;margin-top:10px"><span class="bg-o" style="width:18px;height:18px"></span><span class="bg-n" style="width:18px;height:18px"></span><span class="bg-g" style="width:18px;height:18px"></span></div>
    <p class="label o" style="margin-top:10px">Lorem ipsum<br>dolor sit amet</p>
  </div>
  <div class="abs ph-person" style="left:120px;top:0;width:120px;height:216px" role="img" aria-label="Photo of a customer service representative with headset"></div>
  <div class="abs bg-o" style="left:250px;top:20px;width:120px;height:176px;padding:10px;box-sizing:border-box">
    <p class="head w">Lorem ipsum</p>
    <p class="copy white">Lorem ipsum dolor sit amet, consectetur adipiscing elit, sed do eiusmod tempor incididunt ut labore et dolore.</p>
  </div>
</section>

<section class="slide">
  <div class="abs bg-o" style="left:0;top:0;width:190px;height:216px;padding:18px 14px;box-sizing:border-box">
    <p class="head w">Lorem ipsum</p>
    <p class="copy white">Lorem ipsum dolor sit amet, consectetur adipiscing elit, sed do eiusmod tempor incididunt ut labore.</p>
  </div>
  <div class="abs ph-warm" style="left:190px;top:0;width:194px;height:216px" role="img" aria-label="Photo of stacked coins"></div>
</section>

<section class="slide framed">
  <div class="abs ph-night" style="inset:0" role="img" aria-label="Photo of a waterfront city at night"></div>
  <div class="abs bg-o" style="left:18px;top:70px;width:120px;height:100px;padding:10px;box-sizing:border-box">
    <p class="head w">Lorem ipsum</p>
    <p class="copy white">Lorem ipsum dolor sit amet, consectetur adipiscing elit, sed do eiusmod.</p>
  </div>
</section>

<!-- Row 4 -->
<section class="slide framed">
  <div class="abs ph-sky" style="inset:0" role="img" aria-label="Photo looking up at a skyscraper"></div>
  <div class="abs bg-o" style="left:60px;top:12px;width:200px;height:60px;padding:8px;box-sizing:border-box">
    <p class="head w">Lorem ipsum</p>
    <p class="copy white">Lorem ipsum dolor sit amet, consectetur adipiscing elit.</p>
  </div>
</section>

<section class="slide">
  <div class="abs" style="inset:0;background:linear-gradient(140deg,#f2c84b,#e7e3da 50%,#9aa3ab)" role="img" aria-label="Photo of a hard hat on building plans"></div>
  <span class="abs o" style="left:18px;bottom:40px;font-weight:900;font-size:22px;letter-spacing:1px">QPS</span>
</section>

<section class="slide">
  <h2 class="title">Lorem ipsum dolor sit amet</h2>
  <div class="abs" style="left:40px;right:40px;top:46px"><p class="copy" style="text-align:center">Lorem ipsum dolor sit amet, consectetur adipiscing elit, sed do eiusmod tempor incididunt ut labore.</p></div>
  <div class="icon" style="left:78px;top:80px"><svg><use href="#i-chart"/></svg></div>
  <div class="icon" style="left:178px;top:80px"><svg><use href="#i-gear"/></svg></div>
  <div class="icon" style="left:278px;top:80px"><svg><use href="#i-house"/></svg></div>
  <div class="abs" style="left:50px;top:118px;width:85px"><p class="label o" style="text-align:center">Lorem ipsum</p><p class="copy" style="text-align:center">Lorem ipsum dolor sit amet elit.</p></div>
  <div class="abs" style="left:150px;top:118px;width:85px"><p class="label o" style="text-align:center">Lorem ipsum</p><p class="copy" style="text-align:center">Lorem ipsum dolor sit amet elit.</p></div>
  <div class="abs" style="left:250px;top:118px;width:85px"><p class="label o" style="text-align:center">Lorem ipsum</p><p class="copy" style="text-align:center">Lorem ipsum dolor sit amet elit.</p></div>
  <span class="brand">QPS</span><span class="num">12</span>
</section>

<!-- Row 5 -->
<section class="slide">
  <h2 class="title">Lorem ipsum dolor sit amet</h2>
  <div class="abs" style="left:40px;right:40px;top:44px"><p class="copy" style="text-align:center">Lorem ipsum dolor sit amet, consectetur adipiscing elit.</p></div>
  <div class="icon" style="left:50px;top:72px"><svg><use href="#i-house"/></svg></div>
  <div class="icon" style="left:150px;top:72px"><svg><use href="#i-chart"/></svg></div>
  <div class="icon" style="left:250px;top:72px"><svg><use href="#i-user"/></svg></div>
  <div class="abs" style="left:30px;top:108px;width:320px;display:flex;gap:30px"><p class="copy" style="flex:1">Lorem ipsum dolor sit amet, consectetur elit.</p><p class="copy" style="flex:1">Lorem ipsum dolor sit amet, consectetur elit.</p><p class="copy" style="flex:1">Lorem ipsum dolor sit amet, consectetur elit.</p></div>
  <span class="brand">QPS</span><span class="num">13</span>
</section>

<section class="slide">
  <h2 class="title">Lorem ipsum dolor sit amet</h2>
  <div class="abs" style="left:40px;right:40px;top:44px"><p class="copy" style="text-align:center">Lorem ipsum dolor sit amet, consectetur adipiscing elit.</p></div>
  <div class="icon" style="left:42px;top:72px"><svg><use href="#i-house"/></svg></div>
  <div class="icon" style="left:128px;top:72px"><svg><use href="#i-gear"/></svg></div>
  <div class="icon" style="left:214px;top:72px"><svg><use href="#i-truck"/></svg></div>
  <div class="icon" style="left:300px;top:72px"><svg><use href="#i-chart"/></svg></div>
  <div class="abs" style="left:26px;top:108px;width:340px;display:flex;gap:18px"><p class="label o" style="flex:1">Lorem ipsum</p><p class="label o" style="flex:1">Lorem ipsum</p><p class="label o" style="flex:1">Lorem ipsum</p><p class="label o" style="flex:1">Lorem ipsum</p></div>
  <span class="brand">QPS</span><span class="num">14</span>
</section>

<section class="slide">
  <h2 class="title">Lorem ipsum dolor sit amet</h2>
  <div class="abs" style="left:14px;top:50px;width:110px"><p class="copy">Lorem ipsum dolor sit amet, consectetur adipiscing elit, sed do eiusmod tempor.</p></div>
  <div class="icon" style="left:140px;top:54px"><svg><use href="#i-house"/></svg></div>
  <div class="icon" style="left:200px;top:54px"><svg><use href="#i-gear"/></svg></div>
  <div class="icon" style="left:260px;top:54px"><svg><use href="#i-truck"/></svg></div>
  <div class="icon" style="left:320px;top:54px"><svg><use href="#i-user"/></svg></div>
  <div class="abs" style="left:14px;top:120px;width:356px"><p class="copy">Lorem ipsum dolor sit amet, consectetur adipiscing elit, sed do eiusmod tempor incididunt ut labore et dolore magna aliqua.</p></div>
  <span class="brand">QPS</span><span class="num">15</span>
</section>

<!-- Row 6 -->
<section class="slide">
  <div class="abs ph-street" style="left:8px;top:8px;width:368px;height:200px" role="img" aria-label="Photo of a historic city square"></div>
  <div class="abs bg-o" style="left:8px;top:150px;width:100px;height:40px;padding:6px;box-sizing:border-box"><p class="head w" style="font-size:9px">Lorem ipsum</p><p class="copy white">Lorem ipsum dolor</p></div>
</section>

<section class="slide">
  <div class="abs ph-office" style="left:0;top:0;width:200px;height:216px" role="img" aria-label="Photo of business partners shaking hands"></div>
  <div class="abs bg-nd" style="left:200px;top:0;width:184px;height:216px;padding:16px 14px;box-sizing:border-box">
    <p class="head w">Lorem ipsum</p>
    <p class="copy white">Lorem ipsum dolor sit amet, consectetur adipiscing elit, sed do eiusmod tempor.</p>
    <div style="display:flex;gap:5px;margin-top:12px"><span class="icon" style="position:static;width:16px;height:16px"><svg style="width:10px;height:10px"><use href="#i-check"/></svg></span><span class="icon" style="position:static;width:16px;height:16px"><svg style="width:10px;height:10px"><use href="#i-chart"/></svg></span><span class="icon" style="position:static;width:16px;height:16px"><svg style="width:10px;height:10px"><use href="#i-user"/></svg></span></div>
  </div>
</section>

<section class="slide">
  <h2 class="title left">Lorem ipsum dolor sit amet</h2>
  <div class="abs" style="left:16px;top:48px;width:180px"><p class="copy">Lorem ipsum dolor sit amet, consectetur adipiscing elit, sed do eiusmod tempor incididunt ut labore et dolore magna aliqua. Ut enim ad minim veniam.</p></div>
  <div class="abs ph-office" style="left:210px;top:48px;width:164px;height:120px" role="img" aria-label="Photo of a business meeting"></div>
  <span class="brand">QPS</span><span class="num">18</span>
</section>

<!-- Row 7 -->
<section class="slide">
  <h2 class="title">Lorem ipsum dolor sit amet</h2>
  <div class="abs ph-sky" style="left:14px;top:46px;width:356px;height:60px" role="img" aria-label="Photo of a steel bridge"></div>
  <div class="tile bg-nd" style="left:14px;top:112px;width:114px;height:80px"><p class="lbl">Lorem ipsum</p><p class="copy white">Lorem ipsum dolor sit amet elit.</p></div>
  <div class="tile bg-n" style="left:135px;top:112px;width:114px;height:80px"><p class="lbl">Lorem ipsum</p><p class="copy white">Lorem ipsum dolor sit amet elit.</p></div>
  <div class="tile bg-nd" style="left:256px;top:112px;width:114px;height:80px"><p class="lbl">Lorem ipsum</p><p class="copy white">Lorem ipsum dolor sit amet elit.</p></div>
</section>

<section class="slide">
  <div class="abs" style="left:14px;top:18px;width:130px"><p class="head o">Lorem ipsum</p><p class="copy">Lorem ipsum dolor sit amet, consectetur adipiscing elit, sed do eiusmod.</p></div>
  <div class="abs ph-sky" style="left:160px;top:0;width:224px;height:216px" role="img" aria-label="Photo of a bridge split into a mosaic of panels"></div>
  <div class="abs bg-o" style="left:216px;top:108px;width:56px;height:54px"></div>
  <div class="abs bg-o" style="left:328px;top:54px;width:56px;height:54px"></div>
  <span class="brand">QPS</span>
</section>

<section class="slide">
  <h2 class="title">Lorem ipsum dolor sit amet</h2>
  <div class="tile bg-o" style="left:14px;top:48px;width:84px;height:80px"><p class="lbl">Lorem ipsum dolor sit amet</p><p class="copy white">Lorem ipsum dolor sit amet.</p></div>
  <div class="tile bg-o" style="left:104px;top:48px;width:84px;height:80px"><p class="lbl">Lorem ipsum dolor sit amet</p><p class="copy white">Lorem ipsum dolor sit amet.</p></div>
  <div class="tile bg-o" style="left:194px;top:48px;width:84px;height:80px"><p class="lbl">Lorem ipsum dolor sit amet</p><p class="copy white">Lorem ipsum dolor sit amet.</p></div>
  <div class="tile bg-o" style="left:284px;top:48px;width:84px;height:80px"><p class="lbl">Lorem ipsum dolor sit amet</p><p class="copy white">Lorem ipsum dolor sit amet.</p></div>
  <div class="abs" style="left:14px;top:140px;width:354px"><p class="copy">Lorem ipsum dolor sit amet, consectetur adipiscing elit, sed do eiusmod tempor incididunt ut labore et dolore magna aliqua.</p></div>
  <span class="brand">QPS</span><span class="num">21</span>
</section>

<!-- Row 8 -->
<section class="slide">
  <h2 class="title">Lorem ipsum dolor sit amet</h2>
  <div class="tile bg-od" style="left:14px;top:48px;width:66px;height:140px"><svg><use href="#i-house"/></svg><p class="lbl">Lorem ipsum</p><p class="copy white">Lorem ipsum dolor sit amet.</p></div>
  <div class="tile bg-o" style="left:86px;top:48px;width:66px;height:140px"><svg><use href="#i-chart"/></svg><p class="lbl">Lorem ipsum</p><p class="copy white">Lorem ipsum dolor sit amet.</p></div>
  <div class="tile bg-g" style="left:158px;top:48px;width:66px;height:140px"><svg><use href="#i-gear"/></svg><p class="lbl">Lorem ipsum</p><p class="copy white">Lorem ipsum dolor sit amet.</p></div>
  <div class="tile bg-n" style="left:230px;top:48px;width:66px;height:140px"><svg><use href="#i-truck"/></svg><p class="lbl">Lorem ipsum</p><p class="copy white">Lorem ipsum dolor sit amet.</p></div>
  <div class="tile bg-nd" style="left:302px;top:48px;width:66px;height:140px"><svg><use href="#i-user"/></svg><p class="lbl">Lorem ipsum</p><p class="copy white">Lorem ipsum dolor sit amet.</p></div>
</section>

<section class="slide">
  <h2 class="title">Lorem ipsum dolor sit amet</h2>
  <div class="tile bg-n" style="left:14px;top:48px;width:84px;height:66px"><svg><use href="#i-house"/></svg><p class="lbl">Lorem ipsum</p></div>
  <div class="tile bg-o" style="left:104px;top:48px;width:84px;height:66px"><svg><use href="#i-chart"/></svg><p class="lbl">Lorem ipsum</p></div>
  <div class="tile bg-g" style="left:194px;top:48px;width:84px;height:66px"><svg><use href="#i-gear"/></svg><p class="lbl">Lorem ipsum</p></div>
  <div class="tile bg-nd" style="left:284px;top:48px;width:84px;height:66px"><svg><use href="#i-truck"/></svg><p class="lbl">Lorem ipsum</p></div>
  <div class="tile bg-o" style="left:14px;top:120px;width:84px;height:66px"><p class="copy white">Lorem ipsum dolor sit amet elit.</p></div>
  <div class="tile bg-n" style="left:104px;top:120px;width:84px;height:66px"><p class="copy white">Lorem ipsum dolor sit amet elit.</p></div>
  <div class="tile bg-o" style="left:194px;top:120px;width:84px;height:66px"><p class="copy white">Lorem ipsum dolor sit amet elit.</p></div>
  <div class="tile bg-g" style="left:284px;top:120px;width:84px;height:66px"><p class="copy white">Lorem ipsum dolor sit amet elit.</p></div>
</section>

<section class="slide">
  <h2 class="title">Lorem ipsum dolor sit amet</h2>
  <div class="tile bg-nd" style="left:14px;top:48px;width:84px;height:66px"><svg><use href="#i-house"/></svg><p class="lbl">Lorem ipsum</p></div>
  <div class="tile bg-n" style="left:104px;top:48px;width:84px;height:66px"><svg><use href="#i-user"/></svg><p class="lbl">Lorem ipsum</p></div>
  <div class="tile bg-nd" style="left:194px;top:48px;width:84px;height:66px"><svg><use href="#i-chart"/></svg><p class="lbl">Lorem ipsum</p></div>
  <div class="tile bg-n" style="left:284px;top:48px;width:84px;height:66px"><svg><use href="#i-gear"/></svg><p class="lbl">Lorem ipsum</p></div>
  <div class="tile bg-o" style="left:14px;top:120px;width:84px;height:66px"><svg><use href="#i-truck"/></svg><p class="lbl">Lorem ipsum</p></div>
  <div class="tile bg-od" style="left:104px;top:120px;width:84px;height:66px"><svg><use href="#i-pin"/></svg><p class="lbl">Lorem ipsum</p></div>
  <div class="tile bg-o" style="left:194px;top:120px;width:84px;height:66px"><svg><use href="#i-check"/></svg><p class="lbl">Lorem ipsum</p></div>
  <div class="tile bg-od" style="left:284px;top:120px;width:84px;height:66px"><svg><use href="#i-phone"/></svg><p class="lbl">Lorem ipsum</p></div>
</section>

<!-- Row 9 -->
<section class="slide">
  <div class="abs ph-person" style="left:0;top:0;width:130px;height:216px;background:linear-gradient(160deg,#e8e4dc,#8b8078)" role="img" aria-label="Photo of a man working on a laptop by a window"></div>
  <h2 class="title" style="left:130px">Lorem ipsum dolor sit amet</h2>
  <div class="abs" style="left:150px;top:46px;width:215px"><p class="copy">Lorem ipsum dolor sit amet, consectetur adipiscing elit, sed do eiusmod tempor incididunt.</p></div>
  <div class="icon navy" style="left:160px;top:88px"><svg><use href="#i-house"/></svg></div>
  <div class="icon navy" style="left:210px;top:88px"><svg><use href="#i-chart"/></svg></div>
  <div class="icon navy" style="left:260px;top:88px"><svg><use href="#i-user"/></svg></div>
  <div class="icon navy" style="left:310px;top:88px"><svg><use href="#i-gear"/></svg></div>
  <div class="abs" style="left:150px;top:128px;width:215px"><p class="copy">Lorem ipsum dolor sit amet, consectetur adipiscing elit, sed do eiusmod tempor.</p></div>
  <span class="num">25</span>
</section>

<section class="slide">
  <h2 class="title">Lorem ipsum dolor sit amet</h2>
  <div class="abs ph-person" style="left:50px;top:48px;width:80px;height:80px" role="img" aria-label="Portrait photo of team member"></div>
  <div class="abs ph-person" style="left:152px;top:48px;width:80px;height:80px" role="img" aria-label="Portrait photo of team member"></div>
  <div class="abs ph-person" style="left:254px;top:48px;width:80px;height:80px" role="img" aria-label="Portrait photo of team member"></div>
  <div class="abs" style="left:50px;top:134px;width:80px"><p class="label o">Lorem Ipsum</p><p class="copy">Lorem ipsum dolor sit amet.</p></div>
  <div class="abs" style="left:152px;top:134px;width:80px"><p class="label o">Lorem Ipsum</p><p class="copy">Lorem ipsum dolor sit amet.</p></div>
  <div class="abs" style="left:254px;top:134px;width:80px"><p class="label o">Lorem Ipsum</p><p class="copy">Lorem ipsum dolor sit amet.</p></div>
  <span class="brand">QPS</span><span class="num">26</span>
</section>

<section class="slide">
  <h2 class="title">Lorem ipsum dolor sit amet</h2>
  <div class="abs bg-o" style="left:0;top:48px;width:70px;height:130px;padding:8px;box-sizing:border-box"><p class="label w">Lorem ipsum</p><p class="copy white">Lorem ipsum dolor sit amet.</p></div>
  <div class="abs ph-person" style="left:82px;top:48px;width:66px;height:70px" role="img" aria-label="Portrait photo of team member"></div>
  <div class="abs ph-person" style="left:156px;top:48px;width:66px;height:70px" role="img" aria-label="Portrait photo of team member"></div>
  <div class="abs ph-person" style="left:230px;top:48px;width:66px;height:70px" role="img" aria-label="Portrait photo of team member"></div>
  <div class="abs ph-person" style="left:304px;top:48px;width:66px;height:70px" role="img" aria-label="Portrait photo of team member"></div>
  <div class="abs" style="left:82px;top:124px;width:290px;display:flex;gap:8px"><p class="label o" style="flex:1">Lorem Ipsum</p><p class="label o" style="flex:1">Lorem Ipsum</p><p class="label o" style="flex:1">Lorem Ipsum</p><p class="label o" style="flex:1">Lorem Ipsum</p></div>
  <div class="abs social" style="left:82px;top:150px"><span></span><span></span><span></span></div>
  <span class="brand">QPS</span><span class="num">27</span>
</section>

<!-- Row 10 -->
<section class="slide">
  <h2 class="title">Lorem ipsum dolor sit amet</h2>
  <div class="abs" style="left:40px;right:40px;top:44px"><p class="copy" style="text-align:center">Lorem ipsum dolor sit amet, consectetur adipiscing elit.</p></div>
  <div class="abs ph-person" style="left:18px;top:64px;width:60px;height:60px" role="img" aria-label="Portrait photo of team member"></div>
  <div class="abs ph-person" style="left:89px;top:64px;width:60px;height:60px" role="img" aria-label="Portrait photo of team member"></div>
  <div class="abs ph-person" style="left:160px;top:64px;width:60px;height:60px" role="img" aria-label="Portrait photo of team member"></div>
  <div class="abs ph-person" style="left:231px;top:64px;width:60px;height:60px" role="img" aria-label="Portrait photo of team member"></div>
  <div class="abs ph-person" style="left:302px;top:64px;width:60px;height:60px" role="img" aria-label="Portrait photo of team member"></div>
  <div class="abs" style="left:18px;top:130px;width:344px;display:flex;gap:11px"><p class="label o" style="flex:1">Lorem Ipsum</p><p class="label o" style="flex:1">Lorem Ipsum</p><p class="label o" style="flex:1">Lorem Ipsum</p><p class="label o" style="flex:1">Lorem Ipsum</p><p class="label o" style="flex:1">Lorem Ipsum</p></div>
  <span class="brand">QPS</span><span class="num">28</span>
</section>

<section class="slide">
  <h2 class="title">Lorem ipsum dolor sit amet</h2>
  <div class="abs ph-device" style="left:20px;top:52px;width:150px;height:110px" role="img" aria-label="Desktop monitor showing a property website"></div>
  <div class="abs" style="left:190px;top:56px;width:180px"><p class="label o">Lorem ipsum</p><p class="copy">Lorem ipsum dolor sit amet, consectetur adipiscing elit, sed do eiusmod tempor incididunt ut labore.</p></div>
  <span class="brand">QPS</span><span class="num">29</span>
</section>

<section class="slide">
  <div class="abs bg-o" style="left:0;top:0;width:130px;height:216px;padding:16px 12px;box-sizing:border-box"><p class="head w">Lorem ipsum</p><p class="copy white">Lorem ipsum dolor sit amet, consectetur adipiscing elit, sed do.</p></div>
  <h2 class="title" style="left:130px">Lorem ipsum dolor sit amet</h2>
  <div class="abs ph-device" style="left:160px;top:52px;width:190px;height:120px" role="img" aria-label="Laptop and monitor showing a property website"></div>
  <span class="num">30</span>
</section>

<!-- Row 11 -->
<section class="slide">
  <h2 class="title left">Lorem ipsum dolor</h2>
  <div class="abs bg-o" style="left:0;top:50px;width:210px;height:130px;padding:12px;box-sizing:border-box">
    <p class="copy white">• Lorem ipsum dolor sit amet<br>• Consectetur adipiscing elit<br>• Sed do eiusmod tempor<br>• Ut labore et dolore magna</p>
  </div>
  <div class="abs ph-device" style="left:220px;top:30px;width:150px;height:170px" role="img" aria-label="Hand holding a tablet with app tiles"></div>
  <span class="brand">QPS</span>
</section>

<section class="slide">
  <h2 class="title">Lorem ipsum dolor sit amet</h2>
  <div class="abs" style="left:14px;top:56px;width:110px"><p class="copy">Lorem ipsum dolor sit amet, consectetur adipiscing elit, sed do eiusmod.</p></div>
  <div class="abs bg-o" style="left:130px;top:70px;width:120px;height:100px"></div>
  <div class="abs ph-device" style="left:160px;top:46px;width:60px;height:150px" role="img" aria-label="Smartphone showing app tiles"></div>
  <div class="abs bg-nd" style="left:262px;top:56px;width:108px;height:120px;padding:8px;box-sizing:border-box"><p class="copy white">• Lorem ipsum dolor<br>• Sit amet elit<br>• Sed do eiusmod<br>• Tempor incididunt</p></div>
  <span class="brand">QPS</span><span class="num">32</span>
</section>

<section class="slide bg-nd">
  <h2 class="title white" style="left:200px;right:10px;text-align:left">Lorem ipsum</h2>
  <div class="abs ph-device" style="left:20px;top:30px;width:180px;height:150px" role="img" aria-label="Monitor, tablet and phone showing a responsive website"></div>
  <div class="abs" style="left:212px;top:50px;width:160px"><p class="copy white">Lorem ipsum dolor sit amet, consectetur adipiscing elit, sed do eiusmod tempor incididunt ut labore.</p></div>
</section>

<!-- Row 12 -->
<section class="slide">
  <div class="abs ph-map" style="left:20px;top:20px;width:344px;height:170px" role="img" aria-label="World map showing office locations"></div>
  <div class="abs" style="left:40px;top:40px"><p class="label o">LOREM</p><p class="copy">Lorem ipsum dolor</p></div>
  <div class="abs" style="left:260px;top:40px"><p class="label o">LOREM</p><p class="copy">Lorem ipsum dolor</p></div>
  <div class="abs" style="left:40px;top:140px"><p class="label o">LOREM</p><p class="copy">Lorem ipsum dolor</p></div>
  <div class="abs" style="left:270px;top:140px"><p class="label o">LOREM</p><p class="copy">Lorem ipsum dolor</p></div>
  <span class="brand">QPS</span>
</section>

<section class="slide">
  <h2 class="title">Lorem ipsum dolor sit amet</h2>
  <svg class="abs" style="left:12px;top:62px" width="360" height="50" viewBox="0 0 360 50">
    <polygon points="0,0 110,0 128,25 110,50 0,50" fill="var(--orange)"/>
    <polygon points="120,0 230,0 248,25 230,50 120,50 138,25" fill="var(--navy)"/>
    <polygon points="240,0 342,0 360,25 342,50 240,50 258,25" fill="var(--navy-dk)"/>
    <text x="14" y="29" font-size="7" font-weight="700" fill="#fff" font-family="Lato,sans-serif">Lorem ipsum dolor</text>
    <text x="150" y="29" font-size="7" font-weight="700" fill="#fff" font-family="Lato,sans-serif">Lorem ipsum dolor</text>
    <text x="270" y="29" font-size="7" font-weight="700" fill="#fff" font-family="Lato,sans-serif">Lorem ipsum dolor</text>
  </svg>
  <div class="abs" style="left:12px;top:124px;width:360px;display:flex;gap:14px"><p class="copy" style="flex:1">Lorem ipsum dolor sit amet, consectetur elit.</p><p class="copy" style="flex:1">Lorem ipsum dolor sit amet, consectetur elit.</p><p class="copy" style="flex:1">Lorem ipsum dolor sit amet, consectetur elit.</p></div>
  <span class="brand">QPS</span><span class="num">35</span>
</section>

<section class="slide">
  <h2 class="title">Lorem ipsum dolor sit amet</h2>
  <div class="icon navy" style="left:30px;top:58px"><svg><use href="#i-truck"/></svg></div>
  <div class="icon navy" style="left:100px;top:58px"><svg><use href="#i-house"/></svg></div>
  <div class="icon navy" style="left:170px;top:58px"><svg><use href="#i-user"/></svg></div>
  <div class="icon navy" style="left:240px;top:58px"><svg><use href="#i-chart"/></svg></div>
  <div class="icon navy" style="left:310px;top:58px"><svg><use href="#i-check"/></svg></div>
  <div class="abs bg-o" style="left:14px;top:100px;width:356px;height:4px"></div>
  <div class="abs" style="left:14px;top:112px;width:356px;display:flex;gap:10px"><p class="copy" style="flex:1">Lorem ipsum dolor sit.</p><p class="copy" style="flex:1">Lorem ipsum dolor sit.</p><p class="copy" style="flex:1">Lorem ipsum dolor sit.</p><p class="copy" style="flex:1">Lorem ipsum dolor sit.</p><p class="copy" style="flex:1">Lorem ipsum dolor sit.</p></div>
  <div class="abs bg-o" style="left:14px;top:160px;width:356px;height:22px;display:flex;align-items:center;justify-content:center"><p class="label w">Lorem ipsum dolor sit amet</p></div>
  <span class="brand">QPS</span><span class="num">36</span>
</section>

<!-- Row 13 -->
<section class="slide">
  <h2 class="title">Lorem ipsum dolor sit amet</h2>
  <div class="abs" style="left:14px;top:48px;width:356px;display:grid;grid-template-columns:repeat(4,1fr);gap:3px">
    <div class="cell bg-o w">Lorem</div><div class="cell bg-o w">Ipsum</div><div class="cell bg-o w">Dolor</div><div class="cell bg-o w">Amet</div>
    <div class="cell bg-gl">Lorem</div><div class="cell bg-gl">Ipsum</div><div class="cell bg-gl">Dolor</div><div class="cell bg-gl">Amet</div>
    <div class="cell bg-g w">Lorem</div><div class="cell bg-g w">Ipsum</div><div class="cell bg-g w">Dolor</div><div class="cell bg-g w">Amet</div>
    <div class="cell bg-gl">Lorem</div><div class="cell bg-gl">Ipsum</div><div class="cell bg-gl">Dolor</div><div class="cell bg-gl">Amet</div>
    <div class="cell bg-g w">Lorem</div><div class="cell bg-g w">Ipsum</div><div class="cell bg-g w">Dolor</div><div class="cell bg-g w">Amet</div>
    <div class="cell bg-gl">Lorem</div><div class="cell bg-gl">Ipsum</div><div class="cell bg-gl">Dolor</div><div class="cell bg-gl">Amet</div>
    <div class="cell bg-od w">Lorem</div><div class="cell bg-od w">Ipsum</div><div class="cell bg-od w">Dolor</div><div class="cell bg-od w">Amet</div>
  </div>
  <span class="brand">QPS</span><span class="num">37</span>
</section>

<section class="slide">
  <h2 class="title">Lorem ipsum dolor sit amet</h2>
  <div class="abs" style="left:14px;top:48px;width:356px;display:grid;grid-template-columns:repeat(4,1fr);gap:3px">
    <div class="cell bg-g w">Lorem</div><div class="cell bg-o w">Ipsum</div><div class="cell bg-o w">Dolor</div><div class="cell bg-o w">Amet</div>
    <div class="cell bg-g w">Lorem</div><div class="cell bg-gl">Ipsum</div><div class="cell bg-gl">Dolor</div><div class="cell bg-gl">Amet</div>
    <div class="cell bg-g w">Lorem</div><div class="cell bg-gl">Ipsum</div><div class="cell bg-gl">Dolor</div><div class="cell bg-gl">Amet</div>
    <div class="cell bg-g w">Lorem</div><div class="cell bg-gl">Ipsum</div><div class="cell bg-gl">Dolor</div><div class="cell bg-gl">Amet</div>
    <div class="cell bg-g w">Lorem</div><div class="cell bg-gl">Ipsum</div><div class="cell bg-gl">Dolor</div><div class="cell bg-gl">Amet</div>
    <div class="cell bg-od w">Lorem</div><div class="cell bg-od w">Ipsum</div><div class="cell bg-od w">Dolor</div><div class="cell bg-od w">Amet</div>
  </div>
  <span class="brand">QPS</span><span class="num">38</span>
</section>

<section class="slide">
  <div class="abs bg-o" style="left:0;top:0;width:110px;height:216px;padding:16px 10px;box-sizing:border-box"><p class="head w">Lorem ipsum dolor sit amet</p><p class="copy white">Lorem ipsum dolor sit amet, consectetur adipiscing elit.</p></div>
  <h2 class="title" style="left:110px">Lorem ipsum dolor sit amet</h2>
  <svg class="abs" style="left:124px;top:50px" width="246" height="140" viewBox="0 0 246 140">
    <g fill="var(--orange)">
      <rect x="4" y="30" width="10" height="30"/><rect x="22" y="20" width="10" height="40"/><rect x="40" y="36" width="10" height="24"/><rect x="58" y="14" width="10" height="46"/><rect x="76" y="26" width="10" height="34"/><rect x="94" y="18" width="10" height="42"/><rect x="112" y="32" width="10" height="28"/><rect x="130" y="10" width="10" height="50"/><rect x="148" y="24" width="10" height="36"/><rect x="166" y="16" width="10" height="44"/><rect x="184" y="34" width="10" height="26"/><rect x="202" y="22" width="10" height="38"/><rect x="220" y="12" width="10" height="48"/>
      <rect x="4" y="104" width="10" height="30"/><rect x="22" y="96" width="10" height="38"/><rect x="40" y="110" width="10" height="24"/><rect x="58" y="90" width="10" height="44"/><rect x="76" y="100" width="10" height="34"/><rect x="94" y="94" width="10" height="40"/><rect x="112" y="106" width="10" height="28"/><rect x="130" y="86" width="10" height="48"/><rect x="148" y="98" width="10" height="36"/><rect x="166" y="92" width="10" height="42"/><rect x="184" y="108" width="10" height="26"/><rect x="202" y="96" width="10" height="38"/><rect x="220" y="88" width="10" height="46"/>
    </g>
    <line x1="0" y1="60" x2="246" y2="60" stroke="#ccc"/><line x1="0" y1="134" x2="246" y2="134" stroke="#ccc"/>
  </svg>
</section>

<!-- Row 14 -->
<section class="slide">
  <div class="abs" style="left:14px;top:18px;width:150px"><p class="head o">Lorem ipsum dolor sit amet</p><p class="copy">• Lorem ipsum dolor sit amet<br>• Consectetur adipiscing elit<br>• Sed do eiusmod tempor<br>• Ut labore et dolore magna</p></div>
  <div class="abs bg-o" style="left:180px;top:0;width:204px;height:216px"></div>
  <svg class="abs" style="left:196px;top:24px" width="172" height="140" viewBox="0 0 172 140">
    <g fill="var(--navy)">
      <rect x="6" y="90" width="12" height="50"/><rect x="26" y="70" width="12" height="70"/><rect x="46" y="40" width="12" height="100"/><rect x="66" y="80" width="12" height="60"/><rect x="86" y="20" width="12" height="120"/><rect x="106" y="56" width="12" height="84"/><rect x="126" y="30" width="12" height="110"/><rect x="146" y="64" width="12" height="76"/>
    </g>
  </svg>
  <div class="abs" style="left:196px;top:172px;width:172px"><p class="label w">Lorem ipsum dolor</p></div>
  <span class="brand">QPS</span>
</section>

<section class="slide">
  <h2 class="title">Lorem ipsum dolor sit amet</h2>
  <div class="abs" style="left:20px;top:56px;width:110px"><p class="copy">Lorem ipsum dolor sit amet, consectetur adipiscing elit.</p><p class="o" style="font-size:22px;font-weight:900;margin:14px 0 0">53 %</p></div>
  <svg class="abs" style="left:160px;top:50px" width="200" height="140" viewBox="0 0 200 140">
    <defs><pattern id="sq" width="20" height="20" patternUnits="userSpaceOnUse"><rect width="17" height="17" fill="var(--orange)"/></pattern><pattern id="sqg" width="20" height="20" patternUnits="userSpaceOnUse"><rect width="17" height="17" fill="#fbc48a"/></pattern></defs>
    <rect width="200" height="140" fill="url(#sqg)"/>
    <rect y="60" width="200" height="80" fill="url(#sq)"/>
    <rect y="40" width="120" height="20" fill="url(#sq)"/>
  </svg>
  <span class="brand">QPS</span><span class="num">41</span>
</section>

<section class="slide">
  <h2 class="title">Lorem ipsum dolor sit amet</h2>
  <div class="abs" style="left:16px;top:50px;width:170px"><p class="label o">LOREM IPSUM</p><p class="copy">Lorem ipsum dolor sit amet, consectetur adipiscing elit, sed do eiusmod tempor incididunt ut labore et dolore magna aliqua.</p></div>
  <div class="abs" style="left:198px;top:50px;width:170px"><p class="label o">LOREM IPSUM</p><p class="copy">Lorem ipsum dolor sit amet, consectetur adipiscing elit, sed do eiusmod tempor incididunt ut labore et dolore magna aliqua.</p></div>
  <span class="brand">QPS</span><span class="num">42</span>
</section>

<!-- Row 15 -->
<section class="slide">
  <div class="abs" style="left:14px;top:16px;width:110px"><p class="label o">LOREM IPSUM</p><p class="copy">Lorem ipsum dolor sit amet, consectetur adipiscing elit, sed do eiusmod tempor.</p></div>
  <div class="abs" style="left:137px;top:16px;width:110px"><p class="label o">LOREM IPSUM</p><p class="copy">Lorem ipsum dolor sit amet, consectetur adipiscing elit, sed do eiusmod tempor.</p></div>
  <div class="abs" style="left:260px;top:16px;width:110px"><p class="label o">LOREM IPSUM</p><p class="copy">Lorem ipsum dolor sit amet, consectetur adipiscing elit, sed do eiusmod tempor.</p></div>
  <span class="brand">QPS</span><span class="num">43</span>
</section>

<section class="slide framed">
  <div class="abs ph-sky" style="inset:0" role="img" aria-label="Photo of a business professional in front of office buildings"></div>
  <div class="abs bg-o" style="left:20px;top:120px;width:170px;height:70px;padding:8px;box-sizing:border-box">
    <p class="label w">Lorem ipsum dolor</p>
    <div class="social" style="margin-top:8px"><span style="background:#fff"></span><span style="background:#fff"></span><span style="background:#fff"></span><span style="background:#fff"></span></div>
  </div>
  <span class="brand light" style="left:auto;right:20px;bottom:30px;font-size:14px">QPS</span>
</section>

<section class="slide">
  <div class="abs bg-o" style="left:0;top:0;width:190px;height:216px;padding:20px 14px;box-sizing:border-box">
    <p style="margin:0 0 8px;color:#fff;font-weight:900;font-size:16px;letter-spacing:1px">QPS</p>
    <p class="label w">Quillon Property Services</p>
    <p class="copy white" style="margin-top:6px">120 Harbor Lane, Suite 4, Lorem City<br>Tel. 000 555 0199<br>www.quillonpropertyservices.com</p>
    <div class="social" style="margin-top:10px"><span></span><span></span><span></span><span></span></div>
  </div>
  <div class="abs" style="left:190px;top:0;width:194px;height:216px;background:linear-gradient(135deg,#eceae6,#cfccc6)" role="img" aria-label="Street map with office location"></div>
  <svg class="abs" style="left:276px;top:88px" width="22" height="22" viewBox="0 0 24 24" fill="var(--orange)"><use href="#i-pin"/></svg>
</section>

</main>
</body>
</html>
```